Halvercott Orthodontics business card

Using our existing logo (created with ArtFolio), please create a tasteful, contemporary business card. We are father and daughter orthodontists specializing in braces, clarafit, etc to design healthy, beautiful smiles for children, adolescents, and adults. We would like the design to be family-friendly but not childish.
The final design should include all of the information without looking cluttered (I hope! If necessary to achieve an optimal design, please consider making the card double-sided)
Purple, black, silver on a white card
Please include the following information:
Halvercott Orthodontics (logo)
Marguerite L. Halvercott, DMD
Douglas R. Halvercott, DMD

312 Bramblewood Street
North Andover, MA 01899
978.555.0142

847C Quarry Hollow Street
Methuen, MA 01898
978.555.0187

email frontdesk@halvercottortho.example
website www.halvercottortho.example

```html
<!DOCTYPE html>
<html lang="en">
<head>
<meta charset="utf-8">
<title>Halvercott Orthodontics – Business Card</title>
<link href="https://fonts.googleapis.com/css2?family=Roboto:wght@400;500;700&display=swap" rel="stylesheet">
<style>
  :root {
    --purple: #682f93;
    --ink: #2a2a2a;
    --silver: #8a8a8a;
    --white: #ffffff;
    --backdrop: #3b3b3b;
  }
  html, body {
    margin: 0;
    padding: 0;
    width: 1200px;
    height: 1059px;
    overflow: hidden;
    background: var(--backdrop);
    font-family: "Roboto", Arial, sans-serif;
  }
  .canvas { position: relative; width: 1200px; height: 1059px; }
  .card {
    position: absolute;
    box-sizing: border-box;
    overflow: hidden;
  }
  .card--front { left: 256px; top: 100px; width: 688px; height: 391px; background: var(--white); }
  .card--back { left: 253px; top: 537px; width: 694px; height: 394px; background: var(--purple); }

  .brand {
    position: absolute;
    display: flex;
    align-items: center;
    gap: 14px;
    white-space: nowrap;
    font-weight: 500;
    letter-spacing: 0.5px;
  }
  .brand__dot { border-radius: 50%; flex: none; }
  .card--front .brand { left: 0; right: 0; top: 68px; justify-content: center; font-size: 34px; color: var(--purple); }
  .card--front .brand__dot { width: 26px; height: 26px; background: var(--purple); }
  .card--back .brand { left: 0; right: 0; top: 172px; justify-content: center; font-size: 38px; color: var(--white); }
  .card--back .brand__dot { width: 28px; height: 28px; background: var(--white); }

  .doctor { position: absolute; top: 198px; color: var(--ink); font-size: 16px; line-height: 20px; }
  .doctor--left { right: 366px; text-align: right; }
  .doctor--right { left: 366px; text-align: left; }
  .doctor__name { margin: 0 0 6px; color: var(--purple); font-weight: 700; font-size: 21px; line-height: 30px; white-space: nowrap; }
  .doctor__address { margin: 0; font-style: normal; white-space: nowrap; }
  .doctor__phone { margin: 8px 0 0; display: flex; align-items: center; gap: 6px; }
  .doctor--left .doctor__phone { justify-content: flex-end; }
  .icon { width: 11px; height: 14px; flex: none; }

  .divider { position: absolute; left: 344px; top: 203px; width: 1.5px; height: 91px; background: var(--purple); }

  .contact-band { position: absolute; left: 0; top: 338px; width: 688px; height: 24px; }
  .contact-band__shapes { position: absolute; inset: 0; }
  .contact-band__item {
    position: absolute; top: 0; height: 24px;
    display: flex; align-items: center; gap: 6px;
    color: var(--white); font-size: 15.5px; white-space: nowrap;
  }
  .contact-band__item--email { left: 26px; }
  .contact-band__item--web { right: 26px; }
</style>
</head>
<body>
<main class="canvas">
  <section class="card card--front" aria-label="Card front">
    <div class="brand"><span class="brand__dot"></span>Halvercott Orthodontics</div>

    <div class="doctor doctor--left">
      <p class="doctor__name">Douglas R. Halvercott, DMD</p>
      <address class="doctor__address">847C Quarry Hollow Street<br>Pinecrest, RI 01898</address>
      <p class="doctor__phone">978.555.0187
        <svg class="icon" viewBox="0 0 11 14" aria-hidden="true"><rect x="1" y="0.75" width="9" height="12.5" rx="1.5" fill="none" stroke="#682f93" stroke-width="1.5"/><rect x="4" y="10.3" width="3" height="1.2" fill="#682f93"/></svg>
      </p>
    </div>

    <div class="divider"></div>

    <div class="doctor doctor--right">
      <p class="doctor__name">Marguerite L. Halvercott, DMD</p>
      <address class="doctor__address">312 Bramblewood Street<br>Ashbury Falls, RI 01899</address>
      <p class="doctor__phone">
        <svg class="icon" viewBox="0 0 11 14" aria-hidden="true"><rect x="1" y="0.75" width="9" height="12.5" rx="1.5" fill="none" stroke="#682f93" stroke-width="1.5"/><rect x="4" y="10.3" width="3" height="1.2" fill="#682f93"/></svg>
        978.555.0142</p>
    </div>

    <div class="contact-band">
      <svg class="contact-band__shapes" viewBox="0 0 688 24" preserveAspectRatio="none" aria-hidden="true">
        <polygon points="0,0 352,0 330,24 0,24" fill="#682f93"/>
        <polygon points="358,0 688,0 688,24 336,24" fill="#682f93"/>
      </svg>
      <span class="contact-band__item contact-band__item--email">
        <svg width="12" height="9" viewBox="0 0 12 9" aria-hidden="true"><rect x="0.5" y="0.5" width="11" height="8" fill="none" stroke="#fff"/><polyline points="0.5,0.5 6,5 11.5,0.5" fill="none" stroke="#fff"/></svg>
        frontdesk@halvercottortho.example</span>
      <span class="contact-band__item contact-band__item--web">www.halvercottortho.example
        <svg width="12" height="12" viewBox="0 0 12 12" aria-hidden="true"><circle cx="6" cy="6" r="5.3" fill="none" stroke="#fff" stroke-width="1.2"/><ellipse cx="6" cy="6" rx="2.3" ry="5.3" fill="none" stroke="#fff"/><line x1="0.7" y1="6" x2="11.3" y2="6" stroke="#fff"/></svg>
      </span>
    </div>
  </section>

  <section class="card card--back" aria-label="Card back">
    <div class="brand"><span class="brand__dot"></span>Halvercott Orthodontics</div>
  </section>
</main>
</body>
</html>
```